Land Buying Company Needs Letterhead for Direct Mail Marketing to Land Owners

We are looking for a professional letterhead that we will be including in our direct mail marketing. We will be sending this to land owners who may be interested in selling or purchasing land.

The letterhead needs to be editable. Headers and footers would look nice, but we are open. We would want it to include our address, website, phone, and email info. For right now the address to use for design purposes would the following:

Address: 415 Bramwell Avenue #600
Dallas, TX 75219
Website - www.quillridgeacres.example
Email - info@quillridgeacres.example
Phone - 866-402-ACRE

I have attached our logo zip file that we just had done on Pixel Guild. Let me know what questions you have, and thank you.

```html
<!DOCTYPE html>
<html lang="en">
<head>
<meta charset="utf-8">
<title>Quill Ridge Acres Letterhead</title>
<link rel="stylesheet" href="https://fonts.googleapis.com/css2?family=Montserrat:wght@400;500;600;700&family=Great+Vibes&display=swap">
<style>
  :root {
    --green-dark: #3f5a1e;
    --green-light: #97c93d;
    --ink: #222222;
    --paper: #ffffff;
    --backdrop: #efeff0;
  }
  * { margin: 0; padding: 0; box-sizing: border-box; }
  html, body { width: 714px; height: 1200px; overflow: hidden; background: var(--backdrop); }
  .letterhead {
    position: relative;
    width: 714px;
    height: 1200px;
    background: var(--paper);
    font-family: "Montserrat", sans-serif;
    color: var(--ink);
    overflow: hidden;
  }
  .brand {
    position: absolute;
    left: 48px;
    top: 114px;
    display: flex;
    align-items: center;
    gap: 10px;
  }
  .brand-mark {
    width: 46px;
    height: 46px;
    border-radius: 50%;
    background: var(--green-dark);
  }
  .brand-name {
    font-size: 20px;
    font-weight: 700;
    color: var(--green-light);
    letter-spacing: 0.5px;
    text-transform: uppercase;
    line-height: 1;
  }
  .contact {
    position: absolute;
    top: 117px;
    font-size: 9.5px;
    line-height: 1.15;
  }
  .contact-phone-address { left: 356px; }
  .contact-web { left: 522px; }
  .contact-item {
    display: flex;
    align-items: flex-start;
    gap: 7px;
    margin-bottom: 9px;
  }
  .contact-item svg { width: 10px; height: 10px; flex: none; margin-top: 1px; }
  .contact-item .strong { font-weight: 700; }
  .intro {
    position: absolute;
    left: 48px;
    top: 282px;
  }
  .intro-title {
    font-size: 17px;
    font-weight: 700;
    color: var(--green-dark);
    line-height: 1.2;
  }
  .intro-sub { font-size: 11px; margin-top: 4px; }
  .body-copy {
    position: absolute;
    left: 48px;
    top: 366px;
    width: 621px;
    font-size: 10.6px;
    line-height: 17px;
    text-align: justify;
    hyphens: auto;
  }
  .body-copy p + p { margin-top: 17px; }
  .signoff {
    position: absolute;
    left: 47px;
    top: 823px;
  }
  .signoff-name {
    font-size: 13px;
    font-weight: 700;
    color: var(--green-dark);
  }
  .signoff-script {
    font-family: "Great Vibes", cursive;
    font-size: 19px;
    margin-top: 6px;
  }
  .footer-band {
    position: absolute;
    left: 0;
    bottom: 0;
    width: 714px;
    height: 250px;
    background: linear-gradient(180deg, var(--green-light) 0%, var(--green-dark) 55%, var(--green-dark) 100%);
  }
</style>
</head>
<body>
<main class="letterhead">
  <header>
    <div class="brand">
      <span class="brand-mark"></span>
      <span class="brand-name">Quill Ridge Acres</span>
    </div>

    <div class="contact contact-phone-address">
      <div class="contact-item">
        <svg viewBox="0 0 10 10" aria-hidden="true"><path d="M2.2 0.8 L3.6 2.6 L2.8 3.6 Q4 5.8 6.3 7.2 L7.3 6.4 L9.2 7.8 L8.2 9.3 Q4.5 9 1.9 5.8 Q0.5 3.8 0.8 1.8 Z" fill="var(--green-light)"/></svg>
        <span class="strong">866-402-ACRE</span>
      </div>
      <div class="contact-item">
        <svg viewBox="0 0 10 10" aria-hidden="true"><path d="M5 0.5 A3.4 3.4 0 0 1 8.4 3.9 C8.4 6.3 5 9.6 5 9.6 C5 9.6 1.6 6.3 1.6 3.9 A3.4 3.4 0 0 1 5 0.5 Z M5 2.5 A1.3 1.3 0 1 0 5 5.1 A1.3 1.3 0 1 0 5 2.5 Z" fill="var(--green-light)" fill-rule="evenodd"/></svg>
        <span>415 Bramwell Avenue #600<br>Dallas, TX 75219</span>
      </div>
    </div>

    <div class="contact contact-web">
      <div class="contact-item">
        <svg viewBox="0 0 10 10" aria-hidden="true"><rect x="0.5" y="2" width="9" height="6.4" fill="var(--green-light)"/><path d="M0.8 2.3 L5 5.5 L9.2 2.3" stroke="#fff" stroke-width="0.9" fill="none"/></svg>
        <span>info@quillridgeacres.example</span>
      </div>
      <div class="contact-item">
        <svg viewBox="0 0 10 10" aria-hidden="true"><g fill="none" stroke="var(--green-light)" stroke-width="0.9"><circle cx="5" cy="5" r="4.2"/><ellipse cx="5" cy="5" rx="1.8" ry="4.2"/><path d="M0.8 5 H9.2 M1.5 2.8 H8.5 M1.5 7.2 H8.5"/></g></svg>
        <span>www.quillridgeacres.example</span>
      </div>
    </div>
  </header>

  <section class="intro">
    <h1 class="intro-title">LOREM IPSUM</h1>
    <p class="intro-sub">is simply dummy text of the printing</p>
  </section>

  <section class="body-copy">
    <p>It is a long established fact that a reader will be distracted by the readable content of a page when looking at its layout. The point of using Lorem Ipsum is that it has a more-or-less normal distribution of letters, as opposed to using 'Content here, content here', making it look like readable English. Many desktop publishing packages and web page editors now use Lorem Ipsum as their default model text, and a search for 'lorem ipsum' will uncover many web sites still in their infancy. Various versions have evolved over the years, sometimes by accident, sometimes on purpose (injected humour and the like).</p>
    <p>Contrary to popular belief, Lorem Ipsum is not simply random text. It has roots in a piece of classical Latin literature from 45 BC, making it over 2000 years old. Harold Wexley, a Latin professor at Brierwood College in Westmoor, looked up one of the more obscure Latin words, consectetur, from a Lorem Ipsum passage, and going through the cites of the word in classical literature, discovered the undoubtable source. Lorem Ipsum comes from sections 1.10.32 and 1.10.33 of "de Finibus Bonorum et Malorum" (The Extremes of Good and Evil) by Aurelian, written in 45 BC.</p>
    <p>There are many variations of passages of Lorem Ipsum available, but the majority have suffered alteration in some form, by injected humour, or randomised words which don't look even slightly believable. If you are going to use a passage of Lorem Ipsum, you need to be sure there isn't anything embarrassing hidden in the middle of text. All the Lorem Ipsum generators on the Internet tend to repeat predefined chunks as necessary, making this the first true generator on the Internet. It uses a dictionary of over 200 Latin words, combined with a handful of model sentence structures, to generate Lorem Ipsum which looks reasonable.</p>
    <p>Lorem Ipsum has been the industry's standard dummy text ever since the 1500s, when an unknown printer took a galley of type and scrambled it to make a type specimen book. It has survived not only five centuries, but also the leap into electronic typesetting, remaining essentially unchanged.</p>
  </section>

  <section class="signoff">
    <p class="signoff-name">LOREM IPSUM</p>
    <p class="signoff-script">Is simply dummy</p>
  </section>

  <div class="footer-band" role="img" aria-label="Decorative green footer artwork in light and dark green tones"></div>
</main>
</body>
</html>
```